Flyer-Design für Schwimmtraining für Triathleten
Zielgruppe
Angebot
Schwimmen: als Personal Training, in Kleingruppen oder im Kraulkurs
Schwimmen: Videoanalysen
Triathlon: Trainingspläne, Leistungsdiagnostik
Zielgruppe des Flyers:
Triathleten jeder Leistungsklasse
Flyer ist a) als Auslage in Sportgeschäften, b) als Beilage in Wettkampftüten von Triathlonwettkämpfen gedacht
Aufgabenstellung
Triathleten sind tendenziell technisch orientierte Menschen, vergleichsweise wohlhabend. Schwimmen ist häufig eher die verhasste aber notwendige Teil der drei Disziplinen.
Bitte kein Standardformat für den Flyer.
Die Herausforderung bei einem Flyer als Beigabe zum Wettkampfbeutel: Überlicherweise wird der ganze Packen Werbung achtlos weggeworfen. Design und Format sollen dazu beitragen, dass der Flyer heraussticht und möglichst beachtet wird.
Grundsätzliche Infos: www.kelbrun42.de

```html
<!DOCTYPE html>
<html lang="de">
<head>
<meta charset="utf-8">
<title>Flyer Schwimmtraining – kelbrun42.de</title>
<link href="https://fonts.googleapis.com/css2?family=Open+Sans:wght@400;700;800&display=swap" rel="stylesheet">
<style>
  :root {
    --paper: #ffffff;
    --ink: #222222;
    --brand-blue: #1565b8;
    --white: #ffffff;
    --sky-top: #2f5f8f;
    --sky-mid: #6f8fa8;
    --sun: #f0a63a;
    --hill: #3c3a2a;
    --road: #2a2738;
  }
  * { margin: 0; padding: 0; box-sizing: border-box; }
  html, body {
    width: 849px; height: 1200px; overflow: hidden;
    background: var(--paper);
    font-family: "Open Sans", Arial, sans-serif;
  }
  .sheet { position: relative; width: 849px; height: 1200px; }
  .side-label {
    position: absolute; left: 52px;
    font-size: 16px; font-weight: 400; color: var(--ink);
    letter-spacing: 0.5px;
  }
  .side-label--front { top: 140px; }
  .side-label--back { top: 586px; }

  .flyer {
    position: absolute; left: 50px; width: 737px; height: 375px;
    overflow: hidden;
    box-shadow: 5px 6px 8px rgba(0,0,0,0.35);
  }
  .flyer--front { top: 172px; }
  .flyer--back { top: 618px; }

  .photo {
    position: absolute; inset: 0;
    background:
      radial-gradient(ellipse 160px 110px at 88% 44%, rgba(255,220,140,0.95), rgba(240,166,58,0.6) 45%, rgba(240,166,58,0) 75%),
      linear-gradient(160deg, var(--hill) 0%, var(--hill) 32%, rgba(60,58,42,0) 55%),
      linear-gradient(180deg, var(--sky-top) 0%, var(--sky-mid) 30%, #c98f4a 52%, #5a4a3e 62%, var(--road) 78%, #1f1c2c 100%);
  }

  .headline {
    position: absolute; left: 42px; top: 36px;
    color: var(--white); font-weight: 700;
    font-size: 28px; line-height: 35px; letter-spacing: 0.3px;
  }
  .headline__line { display: block; white-space: nowrap; }
  .headline__line--marked span {
    background: var(--brand-blue); padding: 0 4px 0 2px;
  }
  .brand-name {
    position: absolute; left: 42px; top: 278px;
    color: var(--white); font-weight: 800; font-size: 34px;
  }

  .offer {
    position: absolute; left: 0; top: 0; width: 400px; height: 375px;
    transform: rotate(-2.5deg); transform-origin: 0 30px;
    color: var(--white);
  }
  .offer__band {
    position: absolute; left: -10px; width: 224px; height: 31px;
    background: var(--brand-blue);
    font-weight: 700; font-size: 19px; line-height: 33px;
    letter-spacing: 0.5px;
  }
  .offer__list {
    position: absolute; list-style: none;
    font-weight: 700; font-size: 12px; line-height: 14px;
  }
  .offer__list li { position: relative; padding-left: 8px; }
  .offer__list li.is-bullet::before {
    content: ""; position: absolute; left: 0; top: 4px;
    border-left: 4px solid var(--white);
    border-top: 3px solid transparent; border-bottom: 3px solid transparent;
  }
  .contact {
    position: absolute; left: 100px; top: 300px;
    font-weight: 700; font-size: 12px; line-height: 14px;
  }
</style>
</head>
<body>
<div class="sheet">
  <p class="side-label side-label--front">Vorderseite:</p>
  <section class="flyer flyer--front">
    <div class="photo" role="img" aria-label="Foto: Bergstraße bei Sonnenuntergang mit Läufer und Radfahrer, ein Schwimmer mit blauer Badekappe taucht aus dem Asphalt auf"></div>
    <h1 class="headline">
      <span class="headline__line headline__line--marked"><span>DEIN PERSONAL TRAINER</span></span>
      <span class="headline__line">FÜR SCHWIMMEN, TRIATHLON</span>
      <span class="headline__line">UND AUSDAUERSPORT</span>
    </h1>
    <p class="brand-name">kelbrun42.de</p>
  </section>

  <p class="side-label side-label--back">Rückseite:</p>
  <section class="flyer flyer--back">
    <div class="photo" role="img" aria-label="Foto: Bergstraße bei Sonnenuntergang mit Läufer und Radfahrer, ein Schwimmer mit blauer Badekappe taucht aus dem Asphalt auf"></div>
    <div class="offer">
      <h2 class="offer__band" style="top:36px;padding-left:52px">SCHWIMMEN</h2>
      <ul class="offer__list" style="left:88px;top:76px">
        <li class="is-bullet">Personal Training</li>
        <li>(in Kleingruppen oder im Kraulkurs)</li>
        <li class="is-bullet">Videoanalysen</li>
      </ul>
      <h2 class="offer__band" style="top:124px;padding-left:56px">TRIATHLON</h2>
      <ul class="offer__list" style="left:92px;top:164px">
        <li class="is-bullet">Trainingspläne</li>
        <li class="is-bullet">Leistungsdiagnostik</li>
      </ul>
      <h2 class="offer__band" style="top:198px;padding-left:58px">TRAININGSORTE</h2>
      <ul class="offer__list" style="left:96px;top:238px">
        <li class="is-bullet">München, Mallorca und Lichtenstein</li>
      </ul>
      <h2 class="offer__band" style="top:258px;padding-left:60px">DEIN TRAINER</h2>
      <address class="contact" style="font-style:normal">
        Malte Seewald<br>
        +49 (0)170/5550123<br>
        Malte@kelbrun42.de<br>
        http://www.kelbrun42.de
      </address>
    </div>
  </section>
</div>
</body>
</html>
```